Website redesign for a Cloud Advisory business

We are looking to revisit our existing brand and website, with a view to updating both. Looking for concepts and designs for how the website might look, flow and feel. Current website is: www.brellomint.com.au

Scope and Deliverables: Concept design for the home page and one internal page.

We do not expect you to design all the pages and all the elements of the website at this stage.

This job is not for the full website design, but just for concepts that we can start with when we go into the full website design.

We would love to see a design feature based on our name, logo, or industry, which can run through banners and other collateral (twitter banner, ads on Google, corporate documents etc).

We want the brand to properly depict what we bring/deliver to businesses when consulting to them and this should extend to the colour scheme, logo, font (perhaps updated) and copy (which will be supplied).

Our brand should suitably communicate our ability, knowledge and extensive experience within the Cloud space.

It should express and evoke credibility, knowledge and understanding of the Cloud space, independence, gravitas, reliability, efficiency, trust, expertise, approachability, service delivery but be uncomplicated, practical and use plain speaking language.

Colours that reinforce this might include: Blues, blacks, silver, white, grey and our existing orange.

Website designs that we like or have referenced include:

Varnolift: http://varnolift.com.au/ - This has good information but looks a little amateur in it’s cartoon like design and colour scheme. Also, this seems to be aimed at clients more interested in price than design and what we are going for is a little more high end.

Pendramoor: https://www.pendramoor.com.au/ - This site has merit in its’ setup but little call to action on the home page, especially before the scroll line. I like the set up of the Case Studies page however I’d look to make it more prominent by having it set up 3 across rather than the 4 they have. Something such as this: https://www.qandelby.com/case-studies

Tolvane: http://www.tolvane.com.au/#home4 - This page is a good one as far as selling services and information on the company. I quite like it.

MirefoldIT: http://www.mirefoldit.com.au/ - While I don’t think is particularly creative, it does practically depict the services we offer in a fairly clear way and might be a bit of a basic (albeit dull) template to follow.

JDP: https://store.jdp.com/us/Product-Family/JDP-Advisory-Services/JDP-Cloud-Advisory-Service/p/JDP-Services-Cloud-Advisory - This offers substantial information but is probably a little confusing although the roll-over drop down menus have merit.

ZEV: http://www.zev.net.au/en/services/ - While this in not quite what we are looking for, the colour scheme gives it more gravitas and quality.

As another reference, this website and the way they present their case studies is also something we like, although I’d like them shown 3 up, side by side…. https://www.qandelby.com/case-studies.

We have added a page layout and page purpose document.

Target Market(s)

Corporates, small - medium business, direct referrals, via search results

Industry/Entity Type

Business

Number of Pages Required

1 page

Font styles to use
Sans Serif

Colors
85abd2
0455a3
000000
f37122
5c5c5c

Requirements
Must have
• Website must be mobile device compatible.
• Concept design for the home page.
Nice to have
• We would love to see a design feature based on our name, logo, or industry, which can run through banners and other collateral (twitter banner, ads on Google, corporate documents etc).

```html
<!DOCTYPE html>
<html lang="en">
<head>
<meta charset="utf-8">
<title>Brellomint – Cloud Advisory</title>
<link rel="stylesheet" href="https://fonts.googleapis.com/css2?family=Roboto:wght@400;500&family=Roboto+Condensed&family=Jost:wght@600&family=Nunito:wght@700;800&family=Crimson+Text&family=Open+Sans:ital@0;1&family=Lato&display=swap">
<style>
:root{
  --orange:#f7941d;
  --orange-deep:#f37122;
  --yellow:#fff200;
  --black:#000;
  --white:#fff;
  --rule:#e4e4e4;
  --grey-bar:#333;
  --grey-text:#5c5c5c;
  --blue:#0455a3;
  --sky:#85abd2;
}
*{margin:0;padding:0;box-sizing:border-box}
html,body{width:1171px;height:1200px;overflow:hidden;background:var(--white)}
body{position:relative;font-family:"Roboto",sans-serif}
.abs{position:absolute}
.top-strip{left:0;top:0;width:1171px;height:11px;background:var(--orange)}
.utility-bar{left:0;top:11px;width:1171px;height:39px;background:var(--black)}
.utility-nav{left:50px;top:0;height:39px;display:flex;align-items:center}
.utility-nav a{color:var(--white);font-size:18px;text-decoration:none;padding:0 12px;border-right:2px solid var(--white);line-height:39px}
.utility-nav a:last-child{border-right:none}
.social-top{right:20px;top:0;height:39px;display:flex;align-items:center;gap:6px}
.social-top span{width:11px;height:11px;background:var(--white);border-radius:50%;display:block}
.brand{left:12px;top:76px;height:34px;display:flex;align-items:center;gap:10px}
.brand-name{font-family:"Roboto",sans-serif;font-weight:500;font-size:28px;color:var(--black);letter-spacing:1px;line-height:34px}
.brand-mark{width:16px;height:16px;background:var(--orange-deep);display:block}
.main-nav{top:78px;left:0;height:36px}
.main-nav a{position:absolute;top:0;color:var(--orange);font-size:13px;text-decoration:none;line-height:36px;white-space:nowrap}
.nav-rule{position:absolute;top:0;width:2px;height:30px;background:var(--rule)}
.search{left:1031px;top:84px;color:#ddd;font-size:17px;display:flex;align-items:center;gap:6px}
.search svg{display:block}
.rule{left:0;width:1171px;height:2px;background:var(--rule)}
.hero{left:45px;top:156px;width:1082px;height:308px;background:var(--black);border-top:2px solid var(--orange)}
.hero-visual{position:absolute;left:226px;top:0;right:0;bottom:0;background:linear-gradient(100deg,#0a1f4d 0%,#17407e 35%,#2a6aa4 55%,#b51d3c 78%,#e11f2e 100%)}
.hero-head{position:absolute;left:71px;top:54px;font-family:"Jost",sans-serif;font-weight:600;font-size:68px;line-height:64px;color:var(--white)}
.hero-head .accent{color:var(--yellow)}
.hero-cta{position:absolute;left:75px;top:251px;width:155px;height:44px;border-radius:22px;background:#e6e6e6;border:2px solid #bbb;color:var(--orange);font-size:23px;text-align:center;line-height:40px}
.hero-arrow{position:absolute;top:138px;width:20px;height:26px;background:rgba(40,40,40,.6);color:var(--white);font-size:20px;text-align:center;line-height:26px}
.cards{top:475px;left:0}
.card{position:absolute;top:0;width:368px;height:303px}
.card-head{height:48px;background:var(--black);border-top:2px solid var(--orange);border-radius:0 0 8px 8px;color:var(--orange);font-size:17px;text-align:center;line-height:46px}
.card-body{position:absolute;left:7px;right:10px;top:48px;bottom:0;background:var(--orange);text-align:center;color:var(--white)}
.card-body svg{display:block;margin:29px auto 0}
.card-title{font-family:"Nunito",sans-serif;font-weight:800;font-size:33px;line-height:36px;margin-top:6px}
.card-sub{font-family:"Crimson Text",serif;font-size:11px;line-height:14px}
.card-btn{display:inline-block;margin-top:13px;width:69px;height:19px;border-radius:10px;background:var(--white);color:var(--black);font-family:"Crimson Text",serif;font-size:11px;line-height:19px;box-shadow:2px 2px 3px rgba(0,0,0,.35)}
.dots{display:flex;justify-content:center;gap:2px;margin-top:7px}
.dots span{width:10px;height:12px;border-radius:50%;background:var(--white)}
.dots span.on{background:#ccc}
.section-title{color:var(--orange);font-size:17px}
.client-name{left:27px;top:880px;font-family:"Open Sans",sans-serif;font-weight:400;font-size:15px;color:#d8232a;display:flex;align-items:center;gap:6px;letter-spacing:1px}
.client-name i{width:9px;height:9px;background:#d8232a;display:block}
.quote{left:148px;top:857px;width:395px;font-family:"Open Sans",sans-serif;font-style:italic;font-size:11.6px;line-height:15.5px;color:var(--black)}
.pager{left:542px;top:915px;display:flex;gap:2px}
.pager span{width:8px;height:10px;background:var(--orange)}
.vrule{width:2px;background:var(--rule)}
.offer{left:588px;top:815px;width:346px;text-align:center}
.offer-title{font-family:"Nunito",sans-serif;font-weight:800;font-size:38px;color:var(--orange);line-height:44px;letter-spacing:1px}
.offer-sub{font-family:"Nunito",sans-serif;font-weight:700;font-size:18px;color:var(--orange);line-height:24px}
.signup{left:630px;top:900px;width:284px;height:45px;border-radius:22px;border:2px solid #ccc;overflow:hidden;display:flex}
.signup .field{flex:1;background:#f1f1f1;color:#aaa;font-family:"Nunito",sans-serif;font-size:18px;line-height:41px;padding-left:18px}
.signup .submit{width:95px;background:var(--orange);color:var(--white);font-family:"Nunito",sans-serif;font-size:19px;line-height:41px;text-align:center}
.follow{left:1078px;top:799px;width:51px;height:17px;border-radius:9px;border:1px solid #ccc;background:#f4f4f4;font-size:10px;text-align:center;line-height:15px;color:#333}
.tweet{left:935px;top:821px;width:200px;font-size:10px;line-height:13.4px;color:var(--black);font-family:"Roboto Condensed",sans-serif}
.tweet b{font-family:"Roboto",sans-serif;font-weight:500}
.tweet .muted{color:#999}
.tweet .link{color:#1a9be0}
.tweet-avatar{left:935px;top:827px;width:13px;height:13px;background:#d8232a}
.tweet-text{padding-left:21px}
.tweet-photo{left:938px;top:875px;width:194px;height:86px;background:linear-gradient(90deg,#7c7368,#c9c3ba 45%,#8a8f99)}
.footer{left:0;top:975px;width:1171px;height:167px;background:var(--black);border-top:3px solid var(--orange)}
.footer-col{position:absolute;top:9px;color:var(--white)}
.footer-col h3{font-family:"Open Sans",sans-serif;font-weight:400;font-size:17px;line-height:22px}
.footer-col p,.footer-col li{font-family:"Roboto Condensed",sans-serif;font-size:16px;line-height:20px;list-style:none}
.footer-col p{margin-top:3px}
.footer-col ul{margin-top:3px;padding-left:2px}
.footer-social{display:flex;gap:19px;margin-top:22px;padding-left:6px}
.footer-social span{width:14px;height:14px;border-radius:50%;background:var(--orange);display:block}
.copyright{left:0;top:1145px;width:1171px;height:27px;background:var(--grey-bar);color:var(--white);font-family:"Lato",sans-serif;font-size:17px;text-align:center;line-height:27px}
</style>
</head>
<body>
<div class="abs top-strip"></div>
<div class="abs utility-bar">
  <nav class="abs utility-nav"><a href="#">Home</a><a href="#">Blog</a><a href="#">Media</a></nav>
  <div class="abs social-top" aria-label="Social links"><span></span><span></span><span></span><span></span><span></span></div>
</div>

<header>
  <div class="abs brand">
    <span class="brand-name">BRELLOMINT</span><i class="brand-mark"></i>
  </div>
  <nav class="abs main-nav">
    <span class="nav-rule" style="left:252px"></span><a href="#" style="left:263px">About Us</a>
    <span class="nav-rule" style="left:346px"></span><a href="#" style="left:368px">Speciality</a>
    <span class="nav-rule" style="left:443px"></span><a href="#" style="left:467px">Solutions</a>
    <span class="nav-rule" style="left:546px"></span><a href="#" style="left:566px">Companies</a>
    <span class="nav-rule" style="left:657px"></span><a href="#" style="left:677px">Testimonials</a>
    <span class="nav-rule" style="left:776px"></span><a href="#" style="left:794px">FAQs</a>
    <span class="nav-rule" style="left:840px"></span><a href="#" style="left:859px">Contact Us</a>
    <span class="nav-rule" style="left:944px"></span>
  </nav>
  <div class="abs search">Search
    <svg width="22" height="14" viewBox="0 0 22 14"><circle cx="6" cy="7" r="5" fill="none" stroke="#f7941d" stroke-width="2"/><path d="M11 9 L20 9 M17 9 L17 13" stroke="#f7941d" stroke-width="2" fill="none"/></svg>
  </div>
</header>
<div class="abs rule" style="top:146px"></div>

<section class="abs hero">
  <div class="hero-visual" role="img" aria-label="Hands using a tablet with glowing cloud network icons"></div>
  <h1 class="hero-head">WE DO<br><span class="accent">BRELLOMINT</span><br>FOR YOU</h1>
  <div class="hero-cta">SIGN UP</div>
  <div class="hero-arrow" style="left:4px">&lt;</div>
  <div class="hero-arrow" style="right:6px">&gt;</div>
</section>
<div class="abs rule" style="top:464px"></div>

<section class="abs cards">
  <article class="card" style="left:23px">
    <div class="card-head">Our Products</div>
    <div class="card-body">
      <svg width="174" height="91" viewBox="0 0 174 91"><path d="M22 91 C4 90 0 70 12 60 C20 52 34 48 40 50 C40 32 50 24 62 24 C68 4 96 -2 108 16 C112 22 114 24 116 26 C132 20 150 30 150 50 C166 54 178 74 166 91 Z" fill="#fff"/></svg>
      <div class="card-title">Cloud Solutions</div>
      <div class="card-sub">Safe, Secure and easy to set up</div>
      <div class="card-btn">Sign Up</div>
      <div class="dots"><span></span><span class="on"></span><span></span><span></span></div>
    </div>
  </article>
  <article class="card" style="left:402px">
    <div class="card-head">Products</div>
    <div class="card-body">
      <svg width="174" height="91" viewBox="0 0 174 91"><path d="M22 91 C4 90 0 70 12 60 C20 52 34 48 40 50 C40 32 50 24 62 24 C68 4 96 -2 108 16 C112 22 114 24 116 26 C132 20 150 30 150 50 C166 54 178 74 166 91 Z" fill="#fff"/></svg>
      <div class="card-title">Happy Clients</div>
      <div class="card-sub">Safe, Secure and easy to set up</div>
      <div class="card-btn">Sign Up</div>
      <div class="dots"><span></span><span class="on"></span><span></span><span></span></div>
    </div>
  </article>
  <article class="card" style="left:780px">
    <div class="card-head">Blog</div>
    <div class="card-body">
      <svg width="174" height="91" viewBox="0 0 174 91"><path d="M22 91 C4 90 0 70 12 60 C20 52 34 48 40 50 C40 32 50 24 62 24 C68 4 96 -2 108 16 C112 22 114 24 116 26 C132 20 150 30 150 50 C166 54 178 74 166 91 Z" fill="#fff"/></svg>
      <div class="card-title">Cloud Solutions</div>
      <div class="card-sub">Safe, Secure and easy to set up</div>
      <div class="card-btn">Sign Up</div>
      <div class="dots"><span></span><span class="on"></span><span></span><span></span></div>
    </div>
  </article>
</section>
<div class="abs rule" style="top:787px"></div>

<section class="clients">
  <h2 class="abs section-title" style="left:37px;top:799px;font-weight:400">Our Clients</h2>
  <div class="abs client-name"><i></i>HARLEN LAB</div>
  <p class="abs quote">"We were looking for a package that would be user friendly and suite our needs, we found that in Ledgra. We were concerned with the well indeed. Mireth is a dependable and knowledgeable person in this minefield of accounting software. Highly recommended." - Tomas Verrick</p>
  <div class="abs pager"><span></span><span></span><span></span><span></span></div>
</section>
<div class="abs vrule" style="left:587px;top:798px;height:162px"></div>

<section class="abs offer">
  <div class="offer-title">Get a FREE</div>
  <div class="offer-sub">20 Mins Consultation!</div>
</section>
<div class="abs signup"><div class="field">Enter your E-mail</div><div class="submit">request</div></div>
<div class="abs vrule" style="left:923px;top:798px;height:162px;width:1px"></div>

<section class="tweets">
  <h2 class="abs section-title" style="left:938px;top:797px;font-weight:400">Tweets</h2>
  <div class="abs follow">follow</div>
  <div class="abs tweet-avatar"></div>
  <div class="abs tweet"><div class="tweet-text"><b>Kestrowe Software</b> <span class="muted">@kestroweteam</span><br>We're a big fan of <span class="link">@BrellomintX</span> and their creative <span class="link">#SaaS</span> solutions! <span class="link">#smb</span><br><span class="muted">Retweeted by BrellomintX</span></div></div>
  <div class="abs tweet-photo" role="img" aria-label="Photo of the two consultants at their office desk"></div>
</section>

<footer class="abs footer">
  <div class="footer-col" style="left:22px">
    <h3>About Us</h3>
    <p>We help you pick the right add-on solution for<br>your business. Personalised solution design,<br>set-up, conversion, training and support for you.</p>
  </div>
  <div class="footer-col" style="left:422px">
    <h3>Find Us</h3>
    <p>Melbourne, Victoria<br>1300 472 918<br>info@brellomint.com.au</p>
    <div class="footer-social" aria-label="Social links"><span></span><span></span><span></span><span></span><span></span></div>
  </div>
  <div class="footer-col" style="left:823px">
    <h3>Quick Links</h3>
    <ul><li>Home</li><li>Products</li><li>Contact Us</li><li>Our Clients</li><li>Blog</li></ul>
  </div>
</footer>
<div class="abs copyright">© Brellomint Inc 2016. All rights reserved.</div>
</body>
</html>
```